Business Card Design

Vintage looking Hair Salon, where the customer service is 100%. We are based in a cottage. With shabby chic console tables and beautiful ornate mirrors..and rich brown leather cutting chairs. Chandeliers at the window, and a ornate patchwork sofa.
our clientele are 28years upwards.. Mums with small children.. Ladies that lunch, and men that want more than a barbers and are prepared to pay for our services.
I am looking for a classy business card.. That look expensive.. Where our initials WHP become a visual reference.. I was thinking of cream card initials in black on a embossed tarnished silver.. But I'm open to suggestion. I want,  need the design to be able to work with flyers price list ect.

Willowmere Hair Parlour
27 Fenwick Row
Ardley Green
bN42 6TW
FB thewillowmerehairparlour
Info@thewillowmerhairparlour.co.uk
0208 715 2964

```html
<!DOCTYPE html>
<html lang="en">
<head>
<meta charset="utf-8">
<title>Willowmere Hair Parlour – Business Card</title>
<link rel="stylesheet" href="https://fonts.googleapis.com/css2?family=Oswald:wght@500&family=Open+Sans:wght@600&display=swap">
<style>
  :root {
    --page-bg: #e6e6e6;
    --card-bg: #f6f6f5;
    --card-edge: #8d8d8d;
    --ink: #111111;
  }
  html, body {
    margin: 0;
    padding: 0;
    width: 1200px;
    height: 970px;
    overflow: hidden;
    background: var(--page-bg);
  }
  .business-card {
    position: absolute;
    left: 170px;
    top: 246px;
    width: 860px;
    height: 478px;
    background: var(--card-bg);
    border: 1px solid var(--card-edge);
    box-sizing: border-box;
    color: var(--ink);
    text-align: center;
  }
  .brand-initials {
    position: absolute;
    left: 0;
    right: 0;
    top: 70px;
    margin: 0;
    font-family: "Oswald", sans-serif;
    font-weight: 500;
    font-size: 72px;
    line-height: 90px;
    letter-spacing: 2px;
  }
  .brand-name {
    position: absolute;
    left: 0;
    right: 0;
    top: 200px;
    margin: 0;
    font-family: "Oswald", sans-serif;
    font-weight: 500;
    font-size: 56px;
    line-height: 70px;
    letter-spacing: 1px;
    font-variant: small-caps;
  }
  .contact-icon {
    position: absolute;
    left: 50%;
    transform: translateX(-50%);
    display: block;
  }
  .icon-phone { top: 304px; }
  .icon-mail { top: 354px; }
  .contact-line {
    position: absolute;
    left: 0;
    right: 0;
    margin: 0;
    font-family: "Open Sans", sans-serif;
    font-weight: 600;
    font-size: 19px;
    line-height: 24px;
  }
  .contact-phone { top: 325px; }
  .contact-email { top: 371px; }
  .contact-address { top: 413px; }
</style>
</head>
<body>
  <div class="business-card">
    <p class="brand-initials">WHP</p>
    <h1 class="brand-name">Willowmere Hair Parlour</h1>

    <svg class="contact-icon icon-phone" width="16" height="16" viewBox="0 0 16 16" aria-hidden="true">
      <path d="M3 1.5c1-.8 2-.6 2.4.2l1.2 2.2c.4.7.2 1.3-.4 1.8l-.8.6c.6 1.6 1.6 2.9 3 3.9l.7-.7c.5-.6 1.2-.7 1.8-.3l2.2 1.3c.8.5.9 1.4.2 2.3-1.2 1.4-3 1.6-4.9.3C5.5 11 3.3 8.2 2.2 5.4 1.6 3.8 1.9 2.3 3 1.5z" fill="#111"/>
    </svg>
    <p class="contact-line contact-phone">0208 715 2964</p>

    <svg class="contact-icon icon-mail" width="17" height="12" viewBox="0 0 17 12" aria-hidden="true">
      <rect x="0.6" y="0.6" width="15.8" height="10.8" fill="none" stroke="#111" stroke-width="1.2"/>
      <path d="M0.8 0.8 L8.5 7 L16.2 0.8" fill="none" stroke="#111" stroke-width="1.2"/>
    </svg>
    <p class="contact-line contact-email">Info@thewillowmerhairparlour.co.uk</p>

    <p class="contact-line contact-address">27 Fenwick Row Ardley Green bN42 6TW FB</p>
  </div>
</body>
</html>
```